organic and vegetable shampoo for dogs

we would like to improve the label of an already existing product which will be part of a range of 5 products. we therefore need labels that are identical but modular in relation to the product.
we have developed a range of vegetable and organic products for dog owners.
We prefer that there are no pictures of dogs, only a drawing or symbol that informs the use of the product on dogs.
It is important to highlight the "vegetable" side;
Free of petro-chemical products, paraben-free, dye-free, synthetic fragrance-free, silicone-free.
we can also accept another typo for the name VERA-MOLUND
The bottle is white and round the height of the label is 115mm and the length 147mm; the visible part is 50mm wide.
there are currently 4 different shampoos:
mild shampoo, shampoo for sensitive skin,
color-enhancing shampoos, anti-hair loss shampoo.
A description in French and in English must be provided.

```html
<!DOCTYPE html>
<html lang="fr">
<head>
<meta charset="utf-8">
<title>VERA-MOLUND – Shampooing Doux</title>
<link href="https://fonts.googleapis.com/css2?family=Arimo:wght@400;700&display=swap" rel="stylesheet">
<style>
  :root{
    --page:#f2f3f3;
    --label:#ffffff;
    --teal:#3aa996;
    --teal-deep:#2f9684;
    --purple:#b28ad0;
    --cream:#f3f0e4;
    --white:#ffffff;
  }
  *{box-sizing:border-box;margin:0;padding:0}
  html,body{width:1200px;height:1200px;overflow:hidden}
  body{background:var(--page);font-family:"Arimo",Arial,sans-serif;position:relative}
  .label{
    position:absolute;left:390px;top:60px;width:420px;height:1080px;
    background:var(--label);overflow:hidden;
    box-shadow:0 2px 14px rgba(0,0,0,.08);
  }
  .brand{
    position:absolute;top:60px;left:0;width:100%;text-align:center;
    color:var(--teal);font-weight:700;font-size:30px;letter-spacing:2px;
  }
  .name-fr,.name-en{position:absolute;left:50px}
  .name-fr{top:150px}
  .name-en{top:352px}
  .kicker{color:var(--purple);font-weight:700;font-size:27px;line-height:1}
  .title{color:var(--teal);font-weight:700;font-size:72px;line-height:1;margin-top:4px;letter-spacing:-1px}
  .scent{color:var(--purple);font-size:18px;line-height:1.2;margin-top:4px}
  .name-en .title{margin-top:0}
  .name-en .kicker{font-size:44px;margin-top:2px}
  .use-icon{
    position:absolute;left:50px;top:300px;width:44px;height:44px;border-radius:50%;
    background:linear-gradient(135deg,#efe6f6,#d9c4ea);
  }
  .leaf-art{
    position:absolute;left:300px;top:300px;width:90px;height:240px;border-radius:45px;
    background:linear-gradient(180deg,#f1e8f8,#e2d0ef);
  }
  .band{position:absolute;left:0;top:0;width:420px;height:1080px}
  .claims{
    position:absolute;left:52px;top:620px;width:316px;height:176px;
    background:var(--cream);padding:16px 14px;text-align:center;
    color:var(--teal-deep);font-weight:700;font-size:15px;line-height:1.25;text-transform:uppercase;
  }
  .claims p+p{margin-top:16px}
  .vegetal{
    position:absolute;top:845px;left:0;width:100%;text-align:center;
    color:var(--white);font-weight:700;font-size:36px;line-height:1.05;
  }
  .volume{
    position:absolute;top:968px;left:0;width:100%;text-align:center;
    color:var(--white);font-size:19px;
  }
</style>
</head>
<body>
  <div class="label">
    <svg class="band" viewBox="0 0 420 1080" aria-hidden="true">
      <path fill="var(--teal)" d="M0 560 C40 556 70 548 100 548 L130 540 C170 532 200 520 240 515 L270 508 C310 500 340 490 370 480 L400 474 L420 470 L420 1080 L0 1080 Z"/>
      <path fill="var(--teal)" opacity=".55" d="M0 575 L60 560 L120 552 L90 566 L180 540 L150 556 L260 520 L230 536 L340 500 L310 515 L420 485 L420 500 L0 590 Z"/>
    </svg>

    <div class="brand">VERA-MOLUND</div>

    <div class="name-fr">
      <div class="kicker">Shampooing</div>
      <div class="title">Doux</div>
      <div class="scent">Miel Et Orange Douce</div>
    </div>

    <div class="use-icon" role="img" aria-label="Petit symbole indiquant un usage pour chien"></div>
    <div class="leaf-art" role="img" aria-label="Illustration au trait d'une branche feuillue"></div>

    <div class="name-en">
      <div class="title">Mild</div>
      <div class="kicker">Shampoo</div>
      <div class="scent">Sweet Orange And Honey</div>
    </div>

    <div class="claims">
      <p>Paraben-free | Dye-free | Synthetic fragrance-free | Silicone-free</p>
      <p>Sans paraben | Sans silicone<br>Sans fragrance</p>
    </div>

    <div class="vegetal">100%<br>végétal</div>
    <div class="volume">200ml / 6.7 FL OZ</div>
  </div>
</body>
</html>
```